Clean Chic Simple Black & White One sided Biz Card

I need a business card for my company Brief Matter Arrangers. We are a luxury, white glove service for organizing files for attorneys.
I would like something that is stunningly simple and chic/sexy. This is going to be only one sided. We are going to use raised ink or ink embossing for the printing. So the logo will be raised in black. I am currently waiting to hear back from the printer as to whether or not the logo has to be in all black or can be left in its current state of black with grey initials. Please check our website for inspiration. www.briefmatterarrangers.example.
Thank you so much for your time.

* Please decide whichever title you think looks best(Chief Executive Officer, CEO, or President)
Updates

I really like the designs that make the logo large and the main focus.  
I also like the use of modern, masculine, simple, chic fonts for the slogan and info.

1) No bold font on slogan or info
2) Shrink info to be smaller maybe to make the logo bigger and more the focus
3) Maybe use grey for all the info and slogan so the focus will be on the logo

Thank you so much for your time!!

Target Market(s)

Luxury driven lawyers and their support staff

Industry/Entity Type

Printer

Requirements
Must have
• One sided card

Modern, sleek, masculine, chic, simple font.

Please add our slogan. Refer to file labeled "old logo" to see how we added our slogan under the old logo.
The slogan is, "We Bring Calm to Every Case Folder"

Please include the info below:
Marion Tullbeck (Chief Executive Officer, CEO, or President)
812 North Halvering Avenue, Suite 1400
Calder Springs, Nevada 89517
P: (213)555-0182 F: (213)555-0167
mariont@briefmatterarrangers.example
www.briefmatterarrangers.example

Please refer to attached file labeled "inkpressingembossing requirements" for requirements from my printer. Thank you!
Nice to have
• It can be super simple with just the logo and my info. Or it could maybe have some cool feature. Just clean please.

I would prefer the info not be in bold. I think this will help the Logo stand out as the main focus.

I attached files of how the ink pressing and embossing will look.
Should not have
• No crazy shapes and no color other than black with a white background. The logo should be the focus since it will be embossed.

```html
<!DOCTYPE html>
<html lang="en">
<head>
<meta charset="utf-8">
<title>Brief Matter Arrangers – Business Card</title>
<link rel="stylesheet" href="https://fonts.googleapis.com/css2?family=Abril+Fatface&family=Antonio:wght@200&family=Open+Sans:wght@400&family=Tinos:wght@700&display=swap">
<style>
  :root {
    --ink: #141414;
    --paper: #ffffff;
    --silver: #a9b4b6;
    --slogan-grey: #8f9a9c;
    --rule: #1a1a1a;
  }
  html, body {
    margin: 0;
    padding: 0;
    overflow: hidden;
    background: var(--paper);
  }
  .card {
    position: relative;
    width: 1200px;
    height: 695px;
    background: var(--paper);
    overflow: hidden;
  }
  .edge {
    position: absolute;
    left: 0;
    width: 100%;
    background: var(--ink);
  }
  .edge--top { top: 0; height: 10px; }
  .edge--bottom { bottom: 0; height: 13px; }

  .brand-dot {
    position: absolute;
    left: 508px;
    top: 82px;
    width: 186px;
    height: 186px;
    border-radius: 50%;
    background: var(--silver);
  }
  .brand-name {
    position: absolute;
    left: 0;
    top: 292px;
    width: 100%;
    margin: 0;
    text-align: center;
    font-family: "Abril Fatface", serif;
    font-weight: 400;
    font-size: 37px;
    letter-spacing: 0.3em;
    text-indent: 0.3em;
    color: var(--ink);
    line-height: 1;
  }
  .slogan {
    position: absolute;
    left: 0;
    top: 343px;
    width: 100%;
    margin: 0;
    text-align: center;
    font-family: "Tinos", serif;
    font-weight: 700;
    font-size: 28px;
    color: var(--slogan-grey);
    line-height: 1;
  }

  .person {
    position: absolute;
    right: 777px;
    top: 478px;
    text-align: right;
    font-family: "Antonio", sans-serif;
    font-weight: 200;
    font-size: 31px;
    letter-spacing: 0.12em;
    color: var(--ink);
    line-height: 1.32;
  }
  .person__name, .person__title { display: block; }

  .divider {
    position: absolute;
    left: 466px;
    top: 400px;
    width: 2px;
    height: 236px;
    background: var(--rule);
  }

  .contact {
    position: absolute;
    left: 513px;
    top: 424px;
    margin: 0;
    font-family: "Open Sans", sans-serif;
    font-weight: 400;
    font-size: 25.5px;
    color: var(--ink);
    line-height: 35px;
    font-style: normal;
  }
  .contact__line { display: block; white-space: nowrap; }
</style>
</head>
<body>
  <main class="card">
    <div class="edge edge--top"></div>

    <div class="brand-dot" aria-hidden="true"></div>
    <h1 class="brand-name">BRIEF MATTER ARRANGERS, INC.</h1>
    <p class="slogan">"We Bring Calm to Every Case Folder"</p>

    <div class="person">
      <span class="person__name">MARION TULLBECK</span>
      <span class="person__title">CEO</span>
    </div>

    <div class="divider"></div>

    <address class="contact">
      <span class="contact__line">812 North Halvering Avenue, Suite 1400</span>
      <span class="contact__line">Calder Springs, Nevada 89517</span>
      <span class="contact__line">P: (213)555-0182 F: (213)555-0167</span>
      <span class="contact__line">mariont@briefmatterarrangers.example</span>
      <span class="contact__line">www.briefmatterarrangers.example</span>
    </address>

    <div class="edge edge--bottom"></div>
  </main>
</body>
</html>
```